Veloria....Still Mind, Open Heart

I would like a hologram or golden seed of life as my logo or something along those lines with my business name Veloria and then underneath....Still Mind, Open Heart. Maybe black background....I’m not sure.
On the back, a list of my offerings,
*Harbour of Stillness /Learning to Breathe
*Connection to Source/Self
*Life Changing/Developing
*Plant Medicine consultation
*Conscious Awareness
Veloria_lumen@quillmail.net
Kelwyn: 0427315560
I want my card to look inviting, caring and loving....but with a deep dive into human consciousness 👁💫.
Show me what you got🙏🏽

Designs look the same

```html
<!DOCTYPE html>
<html lang="en">
<head>
<meta charset="utf-8">
<title>Veloria — Business Card</title>
<link rel="stylesheet" href="https://fonts.googleapis.com/css2?family=Jost:wght@400;500;700;800&display=swap">
<style>
  :root {
    --stage: #e9e6e1;
    --ink: #141414;
    --ink-soft: #232323;
    --gold-deep: #8a6a1c;
    --gold: #c9a13b;
    --gold-light: #f1e08c;
    --gold-pale: #f6efc6;
    --text-dark: #1a1a1a;
  }
  * { box-sizing: border-box; margin: 0; padding: 0; }
  html, body { width: 1200px; height: 960px; overflow: hidden; }
  body {
    background: var(--stage);
    font-family: "Jost", sans-serif;
    display: flex;
    flex-direction: column;
    align-items: center;
    justify-content: center;
    gap: 30px;
  }
  .card {
    position: relative;
    width: 760px;
    height: 434px;
    border-radius: 6px;
    overflow: hidden;
    box-shadow: 0 10px 28px rgba(0,0,0,0.22);
  }
  .card-art { position: absolute; inset: 0; width: 100%; height: 100%; display: block; }

  /* Front */
  .front-brand {
    position: absolute;
    left: 0; top: 80px;
    width: 520px;
    display: flex;
    flex-direction: column;
    align-items: center;
  }
  .front-name-row { display: flex; align-items: center; gap: 16px; }
  .brand-dot {
    width: 26px; height: 26px;
    border: 2px solid var(--gold);
    border-radius: 50%;
    flex: none;
  }
  .front-name {
    color: var(--gold);
    font-weight: 500;
    font-size: 46px;
    letter-spacing: 10px;
    text-transform: uppercase;
  }
  .front-tagline {
    margin-top: 14px;
    color: var(--gold);
    font-weight: 500;
    font-size: 24px;
    letter-spacing: 1px;
  }

  /* Back */
  .back-brand {
    position: absolute;
    left: 10px; top: 300px;
    width: 310px;
    display: flex;
    align-items: center;
    justify-content: center;
    gap: 12px;
  }
  .back-name {
    color: var(--gold);
    font-weight: 500;
    font-size: 32px;
    letter-spacing: 5px;
    text-transform: uppercase;
  }
  .back-info {
    position: absolute;
    right: 40px; top: 40px;
    width: 380px;
    color: var(--text-dark);
  }
  .back-title {
    font-weight: 800;
    font-size: 34px;
    letter-spacing: 12px;
    text-transform: uppercase;
    line-height: 1;
  }
  .back-tagline {
    font-weight: 700;
    font-size: 22px;
    margin-top: 4px;
  }
  .offerings {
    list-style: none;
    margin-top: 34px;
    font-size: 17px;
    line-height: 1.45;
  }
  .offerings li { position: relative; padding-left: 18px; }
  .offerings li::before {
    content: "";
    position: absolute;
    left: 0; top: 9px;
    width: 8px; height: 8px;
    border-radius: 50%;
    background: var(--text-dark);
  }
  .contact { margin-top: 18px; text-align: right; font-size: 15px; line-height: 1.7; }
  .contact .phone { font-size: 17px; letter-spacing: 1px; }
</style>
</head>
<body>

  <section class="card card-front">
    <svg class="card-art" viewBox="0 0 760 434" preserveAspectRatio="none">
      <defs>
        <linearGradient id="frontBase" x1="0" y1="0" x2="1" y2="1">
          <stop offset="0" stop-color="#262626"/>
          <stop offset="1" stop-color="#121212"/>
        </linearGradient>
        <linearGradient id="goldBand" x1="0" y1="1" x2="1" y2="0">
          <stop offset="0" stop-color="#8a6a1c"/>
          <stop offset="0.5" stop-color="#f1e08c"/>
          <stop offset="1" stop-color="#c9a13b"/>
        </linearGradient>
      </defs>
      <rect width="760" height="434" fill="url(#frontBase)" role="img" aria-label="Dark floral damask pattern background"/>
      <path d="M150,434 Q430,300 760,222 L760,238 Q440,312 176,434 Z" fill="url(#goldBand)"/>
      <path d="M210,434 Q470,330 760,262 L760,300 Q500,356 290,434 Z" fill="url(#goldBand)"/>
      <path d="M290,434 Q500,356 760,300 L760,434 Z" fill="#151515"/>
    </svg>
    <div class="front-brand">
      <div class="front-name-row">
        <span class="brand-dot"></span>
        <span class="front-name">Veloria</span>
      </div>
      <p class="front-tagline">Still Mind Open Heart</p>
    </div>
  </section>

  <section class="card card-back">
    <svg class="card-art" viewBox="0 0 760 434" preserveAspectRatio="none">
      <defs>
        <linearGradient id="backGold" x1="1" y1="0" x2="0" y2="1">
          <stop offset="0" stop-color="#c9a13b"/>
          <stop offset="0.45" stop-color="#f6efc6"/>
          <stop offset="0.8" stop-color="#e4cd6c"/>
          <stop offset="1" stop-color="#8a6a1c"/>
        </linearGradient>
      </defs>
      <rect width="760" height="434" fill="url(#backGold)"/>
      <path d="M0,210 Q300,160 400,434 L0,434 Z" fill="#8a6a1c" opacity="0.6" transform="translate(6,-6)"/>
      <path d="M0,210 Q300,160 400,434 L0,434 Z" fill="#1c1c1c"/>
    </svg>
    <div class="back-brand">
      <span class="brand-dot"></span>
      <span class="back-name">Veloria</span>
    </div>
    <div class="back-info">
      <h1 class="back-title">Veloria</h1>
      <p class="back-tagline">Still Mind, Open Heart.</p>
      <ul class="offerings">
        <li>Harbour of Stillness /Learning to Breathe</li>
        <li>Connection to Source/Self</li>
        <li>Life Changing/Developing</li>
        <li>Plant Medicine consultation</li>
        <li>Conscious Awareness</li>
      </ul>
      <div class="contact">
        <p class="email">Veloria_lumen@quillmail.net</p>
        <p class="phone">042/731 55 60</p>
      </div>
    </div>
  </section>

</body>
</html>
```